BASIC website restyle: graphic + coding

I need a restyle of our present website. Same contents, but better graphic.
It will be temporary until we'll have defined the strategy and so we'll have the definitive one.
I would need a fast job including coding.

I uploaded some picture that you're free to use.
I also extended of 1 day, no more extensions will be possible.

```html
<!DOCTYPE html>
<html lang="en">
<head>
<meta charset="utf-8">
<title>Verdale</title>
<link href="https://fonts.googleapis.com/css2?family=Questrial&family=Arimo:wght@400;700&family=Nunito:wght@800&display=swap" rel="stylesheet">
<style>
:root{
  --green:#008a4a;
  --green-bar:rgba(0,138,74,.82);
  --ink:#2c3e50;
  --text:#555a5f;
  --footer:#2e3e4c;
  --white:#ffffff;
  --rule:#3a3a3a;
  --dark:#2a2520;
}
*{margin:0;padding:0;box-sizing:border-box}
html,body{width:1200px;height:948px;overflow:hidden}
body{
  font-family:"Arimo",Arial,sans-serif;
  background:linear-gradient(180deg,#6e6e6e 0%,#9a9a9a 35%,#d8d8d8 65%,#ffffff 80%);
  position:relative;
}
.page{
  position:absolute;left:150px;top:0;width:900px;height:948px;
  background:var(--white);
  box-shadow:0 0 12px rgba(0,0,0,.25);
}
.site-header{position:relative;height:94px}
.brand{position:absolute;left:21px;top:20px}
.brand-name{
  font-family:"Questrial",sans-serif;font-size:52px;line-height:52px;
  color:var(--green);letter-spacing:-1px;
}
.main-nav{position:absolute;right:20px;top:37px;display:flex;gap:6px}
.main-nav a{
  display:block;height:31px;line-height:31px;padding:0 17px;
  font-size:14px;color:#222;text-decoration:none;
}
.main-nav a.active{background:var(--green);color:var(--white)}
.hero{
  position:relative;height:351px;
  background:radial-gradient(ellipse at 55% 95%,#d6e89a 0%,#7fbf2e 18%,#3f8a1c 45%,#2a3a12 80%,#1f1a0c 100%);
  text-align:center;color:var(--white);
}
.hero-title{
  position:absolute;left:0;right:0;top:130px;
  font-family:"Nunito",sans-serif;font-weight:800;font-size:50px;line-height:52px;
}
.hero-sub{
  position:absolute;left:0;right:0;top:182px;
  font-family:"Questrial",sans-serif;font-size:48px;line-height:52px;
}
.welcome{position:absolute;left:19px;top:474px;width:554px}
.welcome h1{
  font-family:"Questrial",sans-serif;font-size:23px;color:var(--ink);
  letter-spacing:.5px;margin-bottom:12px;
}
.welcome h1 span{color:var(--green)}
.welcome p{
  font-size:13.5px;line-height:16px;color:var(--text);text-align:justify;margin-bottom:15px;
}
.feature{position:absolute;top:637px;width:253px;height:136px;overflow:hidden}
.feature-forest{left:19px;background:linear-gradient(160deg,#7a5e44,#b5916a 45%,#5b4330)}
.feature-agri{left:319px;background:linear-gradient(180deg,#7d9cd0 0%,#c9cdd3 45%,#6f7a5e 100%)}
.feature-label{
  position:absolute;left:0;right:0;bottom:0;height:31px;background:var(--green-bar);
  color:var(--white);font-weight:700;font-size:17px;
  line-height:31px;padding-left:9px;
}
.feature-label svg{position:absolute;right:12px;top:5px}
.sidebar{position:absolute;left:626px;top:472px;width:259px}
.side-block{margin-bottom:26px}
.side-title{
  font-family:"Questrial",sans-serif;font-size:23px;line-height:22px;
  color:var(--ink);font-weight:700;letter-spacing:.5px;padding-bottom:4px;
}
.side-title .lead{color:var(--green);display:block}
.partner-rule{border-bottom:1px solid var(--rule)}
.ref-rule{border-bottom:1px solid var(--green)}
.partner{display:flex;align-items:center;gap:11px;margin-top:13px}
.partner-badge{width:63px;height:63px;border-radius:50%;background:#0f7f86;flex:none}
.partner-name{font-size:13.5px;line-height:16px;color:#222;margin-top:12px}
.reference{margin-top:18px;display:flex;align-items:center;gap:14px}
.reference-badge{width:46px;height:46px;border:4px solid var(--dark);flex:none}
.reference-name{
  font-family:"Nunito",sans-serif;font-weight:800;font-size:22px;
  color:var(--dark);letter-spacing:2px;white-space:nowrap;
}
.site-footer{
  position:absolute;left:0;bottom:0;width:900px;height:81px;background:var(--footer);
  color:var(--white);text-align:center;
}
.footer-address{font-size:14px;margin-top:20px}
.footer-copy{font-size:12px;margin-top:10px}
</style>
</head>
<body>
<div class="page">
  <header class="site-header">
    <div class="brand">
      <div class="brand-name">VERDALE</div>
    </div>
    <nav class="main-nav">
      <a class="active" href="#">Home</a>
      <a href="#">Emberguard</a>
      <a href="#">FieldSense</a>
      <a href="#">Technology</a>
      <a href="#">Contact us</a>
    </nav>
  </header>

  <section class="hero" role="img" aria-label="Sunlit green forest path lined with tall trees">
    <div class="hero-title">Emberguard</div>
    <div class="hero-sub">Forest Fires Prediction</div>
  </section>

  <section class="welcome">
    <h1>Welcome to <span>VERDALE</span></h1>
    <p>Lorem ipsum dolor sit amet, consectetur adipiscing elit. Proin dapibus imperdiet libero at fringilla. Maecenas est nunc, pretium a iaculis sed, blandit ut ligula. Nunc sagittis massa vitae diam imperdiet rutrum.</p>
    <p>Nullam ac fermentum libero, vehicula lobortis lectus. Suspendisse volutpat pulvinar dui a consequat.</p>
  </section>

  <a class="feature feature-forest" href="#" role="img" aria-label="Sensor probe standing in dry fallen leaves on the forest floor">
    <span class="feature-label">Forest Fires Prediction
      <svg width="22" height="22" viewBox="0 0 22 22"><circle cx="11" cy="11" r="11" fill="#1f4d33"/><path d="M9 6l5 5-5 5" stroke="#fff" stroke-width="2.4" fill="none"/></svg>
    </span>
  </a>
  <a class="feature feature-agri" href="#" role="img" aria-label="Weather station among blossoming orchard trees">
    <span class="feature-label">Agriculture
      <svg width="22" height="22" viewBox="0 0 22 22"><circle cx="11" cy="11" r="11" fill="#1f4d33"/><path d="M9 6l5 5-5 5" stroke="#fff" stroke-width="2.4" fill="none"/></svg>
    </span>
  </a>

  <aside class="sidebar">
    <div class="side-block">
      <h2 class="side-title partner-rule"><span class="lead">Verdale</span>Scientific Partner:</h2>
      <div class="partner">
        <div class="partner-badge"></div>
        <div class="partner-name">Alpine Institute for Woodland, Snow and Terrain Studies</div>
      </div>
    </div>
    <div class="side-block">
      <h2 class="side-title ref-rule"><span class="lead">Verdale</span>Scientific Reference:</h2>
      <div class="reference">
        <div class="reference-badge"></div>
        <div class="reference-name">ALPS BOARD</div>
      </div>
    </div>
  </aside>

  <footer class="site-footer">
    <div class="footer-address">Verdale SA - Via dei Larici 22 - CH6900 Lugano (Parco Scienza), Switzerland - hello@verdale-lab.ch</div>
    <div class="footer-copy">Copyright © 2013 Verdale. All Rights Reserved.</div>
  </footer>
</div>
</body>
</html>
```